Welbourne Dental, P.C. New stationary and business card for modern Dental Office

We need a new stationary/envelope/business card design using our newly designed logo. We are looking for an upscale look. Our new logo is used on our signage, using black as the background and white for the lettering. We would like the stationary to have black, white, possible greys or silver. We are looking for a letterhead, envelope, and business card design for three different employees, as well as a 4th card, same design, but just general with no employee name.

Project Deadline Extended
Reason: We began this project in the middle of our move into our new office. Things got pretty hectic and we just didn't have the time to go through designs. We now settled in and finally eliminated the designs that didn't work for us. We would like to extend the project another 5 days, and then finalize our decision. Most of the submissions showed business cards alone, with no stationary designs. Our original request was for stationary and business cards. Please keep this in mind.

Target Market(s)

Dental patients expecting high quality, cosmetic dentistry

Industry/Entity Type

Business

Contact Information for Business Card

Will need a design using our logo. All cards will be the same, other than that one card will have Office Managers name, One for the Doctor, Hygienist,
1. Office Manager - Marisol Dubrovka
2. Hygienist - Kayleigh Morrow
3. Gordon T. Welbourne, D.D.S.
4. One general one with no staff names

Font styles to use
Other font styles liked:
• see upload

Colors
000000
1b1b1b
757575
c9c9c9
e8e8e8
ffffff

Requirements
Must have
• -Logo
• -Phone number (718)555-0193
• -Address: 4352 63rd Ave
• Lower Level
• Brooklyn, NY 11290

```html
<!DOCTYPE html>
<html lang="en">
<head>
<meta charset="utf-8">
<title>Welbourne Dental, P.C. — Stationery Set</title>
<link href="https://fonts.googleapis.com/css2?family=Lato:wght@400;700&display=swap" rel="stylesheet">
<style>
:root{
  --black:#000000;
  --ink:#1b1b1b;
  --grey-dark:#444444;
  --grey:#757575;
  --silver:#c9c9c9;
  --canvas:#bdbdbd;
  --white:#ffffff;
}
*{margin:0;padding:0;box-sizing:border-box}
html,body{width:1200px;height:1008px;overflow:hidden}
body{background:var(--canvas);font-family:'Lato',sans-serif;position:relative}
.sheet{position:absolute;box-shadow:2px 3px 4px rgba(0,0,0,.35);overflow:hidden}
.dark{background:var(--black);color:var(--white)}
.light{background:var(--white);color:var(--ink)}

/* business cards */
.card{left:29px;width:321px;height:183px}
.card--contact-dark{top:34px}
.card--contact-light{top:235px}
.card--logo{top:434px}
.card .person{position:absolute;left:22px;top:57px}
.card .name{font-size:13px;font-weight:700}
.card .role{font-size:10px;color:var(--grey);margin-top:2px}
.card--contact-dark .role{color:#9a9a9a}
.card .divider{position:absolute;left:124px;top:60px;width:1px;height:101px;background:currentColor;opacity:.8}
.card .details{position:absolute;left:133px;top:62px;font-size:10.5px;line-height:15px}
.card .details .row{display:flex;align-items:center;gap:4px}
.card .details .gap{height:8px}
.card .details .address{font-size:11.5px;line-height:13px;margin-top:3px}
.icon{width:9px;height:9px;flex:none}
.card-band{position:absolute;left:0;bottom:0;width:321px;height:15px}

/* logo lockup */
.logo{position:absolute;display:flex;align-items:center;font-family:'Lato',sans-serif;font-weight:400;color:var(--white);white-space:nowrap}
.logo .mark{border:2px solid var(--white);border-radius:50%;flex:none}
.logo--card{left:64px;top:70px;gap:10px;font-size:17px}
.logo--card .mark{width:46px;height:46px}
.logo--folder{left:76px;top:206px;gap:12px;font-size:21px}
.logo--folder .mark{width:58px;height:58px}
.logo--small{gap:5px;font-size:8px}
.logo--small .mark{width:20px;height:20px;border-width:1px}

/* folder */
.folder{left:392px;top:34px;width:378px;height:490px}

/* letterhead */
.letterhead{left:792px;top:37px;width:378px;height:490px}
.letterhead .header{position:absolute;left:0;top:0;width:100%;height:64px;background:var(--black)}
.letterhead .logo{left:150px;top:22px}
.letterhead .footer-info{position:absolute;left:42px;top:460px;font-size:5px;display:flex;align-items:center;gap:4px;color:var(--ink)}
.letterhead .footer-info .sep{width:1px;height:7px;background:var(--ink)}
.letterhead .footer-band{position:absolute;left:0;top:472px;width:378px;height:18px}

/* envelopes */
.envelope{top:686px;width:470px;height:239px}
.envelope--front{left:139px}
.envelope--back{left:658px}
.envelope .header{position:absolute;left:0;top:0;width:100%;height:66px;background:var(--black)}
.envelope--front .logo{left:18px;top:23px}
.envelope .return{position:absolute;left:136px;top:16px;padding-left:6px;border-left:1px solid var(--white);color:var(--white);font-size:6.5px;line-height:8px}
.envelope .return .row{display:flex;align-items:center;gap:3px;margin-bottom:7px}
.envelope .flap{position:absolute;left:0;top:0}
.envelope--back .logo{left:208px;top:17px}
</style>
</head>
<body>

<!-- business card: contact, dark -->
<section class="sheet card card--contact-dark dark">
  <div class="person"><p class="name">Tobias Renfrew</p><p class="role">Director</p></div>
  <div class="divider"></div>
  <div class="details">
    <p class="row"><svg class="icon" viewBox="0 0 10 10"><rect x="2.5" y="0.5" width="5" height="9" rx="1" fill="none" stroke="#fff"/></svg>(718)555-0276</p>
    <p class="row"><svg class="icon" viewBox="0 0 10 10"><path d="M1 3 Q5 0 9 3 L8 4.5 L6.5 3.5 L3.5 3.5 L2 4.5Z M2 5 H8 V9 H2Z" fill="#fff"/></svg>(718)555-0193</p>
    <div class="gap"></div>
    <p class="row"><svg class="icon" viewBox="0 0 10 10"><rect x="0.5" y="2" width="9" height="6" fill="#fff"/><path d="M0.5 2 L5 5.5 L9.5 2" fill="none" stroke="#000"/></svg>info@welbournedental.com</p>
    <p class="row"><svg class="icon" viewBox="0 0 10 10" fill="none" stroke="#fff" stroke-width=".8"><circle cx="5" cy="5" r="4.3"/><ellipse cx="5" cy="5" rx="2" ry="4.3"/><path d="M0.7 5H9.3"/></svg>www.welbournedental.com</p>
    <p class="address">4352 63rd Ave<br>Lower Level, Brooklyn, NY 11290</p>
  </div>
</section>

<!-- business card: contact, light -->
<section class="sheet card card--contact-light light">
  <div class="person"><p class="name">Tobias Renfrew</p><p class="role">Director</p></div>
  <div class="divider"></div>
  <div class="details">
    <p class="row"><svg class="icon" viewBox="0 0 10 10"><rect x="2.5" y="0.5" width="5" height="9" rx="1" fill="none" stroke="#1b1b1b"/></svg>(718)555-0276</p>
    <p class="row"><svg class="icon" viewBox="0 0 10 10"><path d="M1 3 Q5 0 9 3 L8 4.5 L6.5 3.5 L3.5 3.5 L2 4.5Z M2 5 H8 V9 H2Z" fill="#1b1b1b"/></svg>(718)555-0193</p>
    <div class="gap"></div>
    <p class="row"><svg class="icon" viewBox="0 0 10 10"><rect x="0.5" y="2" width="9" height="6" fill="#1b1b1b"/><path d="M0.5 2 L5 5.5 L9.5 2" fill="none" stroke="#fff"/></svg>info@welbournedental.com</p>
    <p class="row"><svg class="icon" viewBox="0 0 10 10" fill="none" stroke="#1b1b1b" stroke-width=".8"><circle cx="5" cy="5" r="4.3"/><ellipse cx="5" cy="5" rx="2" ry="4.3"/><path d="M0.7 5H9.3"/></svg>www.welbournedental.com</p>
    <p class="address">4352 63rd Ave<br>Lower Level, Brooklyn, NY 11290</p>
  </div>
  <svg class="card-band" viewBox="0 0 321 15" preserveAspectRatio="none">
    <rect width="321" height="15" fill="#000"/>
    <polygon points="0,0 213,0 205,15 0,15" fill="#444"/>
    <polygon points="213,0 218,0 210,15 205,15" fill="#fff"/>
  </svg>
</section>

<!-- business card: logo side -->
<section class="sheet card card--logo dark">
  <div class="logo logo--card">Welbourne Dental, P.C.<span class="mark"></span></div>
</section>

<!-- presentation folder -->
<section class="sheet folder dark">
  <div class="logo logo--folder">Welbourne Dental, P.C.<span class="mark"></span></div>
</section>

<!-- letterhead -->
<section class="sheet letterhead light">
  <div class="header">
    <div class="logo logo--small">Welbourne Dental, P.C.<span class="mark"></span></div>
  </div>
  <div class="footer-info">
    <svg class="icon" viewBox="0 0 10 10" style="width:5px;height:5px"><path d="M1 3 Q5 0 9 3 L8 4.5 L6.5 3.5 L3.5 3.5 L2 4.5Z M2 5 H8 V9 H2Z" fill="#1b1b1b"/></svg>
    <span>(718)555-0193</span><span class="sep"></span><span>4352 63rd Ave, Lower Level, Brooklyn, NY 11290</span>
  </div>
  <svg class="footer-band" viewBox="0 0 378 18" preserveAspectRatio="none">
    <rect width="378" height="18" fill="#000"/>
    <polygon points="0,0 243,0 233,18 0,18" fill="#444"/>
    <polygon points="243,0 249,0 239,18 233,18" fill="#fff"/>
  </svg>
</section>

<!-- envelope front -->
<section class="sheet envelope envelope--front light">
  <div class="header">
    <div class="logo logo--small">Welbourne Dental, P.C.<span class="mark"></span></div>
    <div class="return">
      <p class="row"><svg class="icon" viewBox="0 0 10 10" style="width:6px;height:6px"><path d="M1 3 Q5 0 9 3 L8 4.5 L6.5 3.5 L3.5 3.5 L2 4.5Z M2 5 H8 V9 H2Z" fill="#fff"/></svg>(718)555-0193</p>
      <p>4352 63rd Ave<br>Lower Level<br>Brooklyn, NY 11290</p>
    </div>
  </div>
</section>

<!-- envelope back -->
<section class="sheet envelope envelope--back light">
  <svg class="flap" width="470" height="66" viewBox="0 0 470 66">
    <path d="M0,0 H470 C448,22 432,58 400,61 C330,64 150,64 75,61 C45,59 25,30 0,0Z" fill="#000"/>
  </svg>
  <div class="logo logo--small">Welbourne Dental, P.C.<span class="mark"></span></div>
</section>

</body>
</html>
```